amber tide alliance non profit

I need a simple static website for a non-profit organization that includes blog capacity through Wordpress. The non-profit organization provides education and funding for alternative births and post natal care (doulas and mid-wives) for women. I have the domain name already but not the hosting. I've also set up a gmail account to link to the contact me page.
Updates

Also, would love warm colors.  Background can be white but toolbar and other accents could be peachy warm, tan / mauvish earthy colors.

Thanks.

Target Market(s)

The webstie will be for women who are going through the birthing process or have just given birth. Targeted toward women 16 to 50. The site will include various international outreach programs

Industry/Entity Type

Non Profit

Number of Pages Required

5+ pages

Requirements
Must have
• I want a site that I can control content after it has been designed. So I can add and change copy once it's up. It also must have photo and blog capacity (blog through Wordpress). Toolbar should include (with corresponding pages behind it that I will later include more info that I can update myself) Home, About, Resources / Links, Workshops, Members/Board, Donate Here-sponsors, Forum, International Outreach and somewhere on the homepage: Membership sign-up, Contact.
• The copy attached can be used on the home page.  Then where it explains about the founder, can be in the About section.

• Use warm tones - like peaches or mauvish earthy tan colors for the Toolbars.  (Background can be white.) 
• Use logo (attached) in banner on left and tagline: 
• Non-profit organization providing pre- and postnatal care for women.

• Would like the black and white photo with the mom's hands and baby's feet used as a constant photo and/or in the banner.
Nice to have
• Video capacity for me to add information.  This can be on the blog (through wordpress.)
Should not have
• No stiff, rigid lines.

```html
<!DOCTYPE html>
<html lang="en">
<head>
<meta charset="utf-8">
<title>Amber Tide Alliance</title>
<link rel="stylesheet" href="https://fonts.googleapis.com/css2?family=Arimo:wght@400;700&family=Cinzel:wght@400&family=Tinos&display=swap">
<style>
  :root {
    --page-cream: #e4dec9;
    --band-sage: #7c8070;
    --band-sage-dark: #6c7062;
    --header-black: #000000;
    --content-olive: #87836e;
    --content-olive-light: #8f8b76;
    --footer-olive: #958f79;
    --tab-paper: #ece6d2;
    --tab-ink: #8c8873;
    --tab-tape: #6e6422;
    --text-light: #f4f1e8;
    --logo-ink: #4f4a41;
  }
  * { box-sizing: border-box; margin: 0; padding: 0; }
  html, body { width: 1200px; height: 1196px; overflow: hidden; }
  body {
    position: relative;
    background: var(--page-cream);
    font-family: "Arimo", Arial, sans-serif;
  }
  .backdrop-band {
    position: absolute; left: 0; top: 170px; width: 1200px; height: 434px;
    background: linear-gradient(135deg, var(--band-sage) 0%, var(--band-sage-dark) 50%, var(--band-sage) 100%);
  }
  .brand {
    position: absolute; left: 87px; top: 14px;
    display: flex; flex-direction: column; align-items: center; gap: 6px;
  }
  .brand-dot {
    width: 88px; height: 88px; border-radius: 50%;
    border: 9px solid var(--logo-ink);
  }
  .brand-name {
    font-size: 17px; font-weight: 700; color: var(--logo-ink);
    letter-spacing: -0.2px;
  }
  .site {
    position: absolute; left: 80px; top: 143px; width: 1040px; height: 989px;
    box-shadow: 0 0 8px rgba(0,0,0,0.35);
  }
  .masthead {
    position: relative; height: 329px; background: var(--header-black);
  }
  .main-nav { position: absolute; left: 0; top: 0; width: 100%; height: 80px; }
  .nav-tab {
    position: absolute; top: 33px; width: 113px; height: 41px;
    background: var(--tab-paper);
    border-radius: 6px 14px 5px 12px / 8px 4px 10px 6px;
    font-family: "Cinzel", "Times New Roman", serif;
    font-size: 13px; line-height: 14px; color: var(--tab-ink);
    display: flex; align-items: center; justify-content: center; text-align: center;
  }
  .nav-tab::before {
    content: ""; position: absolute; left: -6px; top: -10px;
    width: 34px; height: 14px; background: var(--tab-tape); opacity: 0.85;
    transform: rotate(-28deg);
  }
  .nav-tab.tilt-a { transform: rotate(2deg); }
  .nav-tab.tilt-b { transform: rotate(-2deg); }
  .hero-photo { position: absolute; }
  .hero-photo.hands-feet {
    left: 2px; top: 74px; width: 270px; height: 240px;
    background: radial-gradient(ellipse at 45% 45%, #bdbdbd 0%, #6a6a6a 45%, #000 75%);
  }
  .hero-photo.expecting-mother {
    left: 847px; top: 74px; width: 188px; height: 255px;
    background: radial-gradient(ellipse at 55% 60%, #9a9a9a 0%, #505050 45%, #000 80%);
  }
  .tagline {
    position: absolute; left: 293px; top: 124px; width: 560px;
    font-family: "Tinos", "Times New Roman", serif;
    font-size: 31px; line-height: 34px; color: #fff;
  }
  .content {
    position: relative; height: 505px;
    background: radial-gradient(ellipse at 40% 30%, var(--content-olive-light) 0%, var(--content-olive) 70%);
  }
  .intro {
    position: absolute; left: 70px; top: 57px; width: 610px;
    font-size: 13.4px; line-height: 16.4px; color: var(--text-light);
  }
  .intro p + p { margin-top: 16px; }
  .feature-list { position: absolute; left: 729px; top: 30px; width: 244px; }
  .feature { margin-bottom: 16px; text-align: center; }
  .feature-photo {
    display: block; width: 244px; height: 117px;
    box-shadow: 0 2px 6px rgba(0,0,0,0.35);
  }
  .feature-photo.outreach { background: linear-gradient(135deg, #f6f3ef 0%, #e0b7a0 40%, #2c9b3b 55%, #f8f6f3 80%); }
  .feature-photo.volunteers { background: linear-gradient(120deg, #d7a89a 0%, #f0d6cc 45%, #e6bfb3 70%, #f4e6e0 100%); }
  .feature-photo.news { background: linear-gradient(135deg, #f1f2f5 0%, #3a7ec4 35%, #e6ecf4 60%, #9bb9da 100%); }
  .feature-caption {
    margin-top: 10px;
    font-size: 12.5px; font-weight: 700; color: #fff;
    font-variant: small-caps; letter-spacing: 0.3px;
  }
  .site-footer {
    position: relative; height: 155px; background: var(--footer-olive);
  }
  .copyright {
    position: absolute; right: 20px; top: 112px;
    font-size: 13.5px; font-weight: 700; color: #fff;
  }
</style>
</head>
<body>
  <div class="backdrop-band"></div>

  <div class="brand">
    <span class="brand-dot"></span>
    <span class="brand-name">Amber Tide Alliance</span>
  </div>

  <div class="site">
    <header class="masthead">
      <nav class="main-nav">
        <a class="nav-tab tilt-a" style="left:192px; top:41px;">Home</a>
        <a class="nav-tab tilt-b" style="left:333px;">About</a>
        <a class="nav-tab tilt-a" style="left:471px;">Resources<br>/Links</a>
        <a class="nav-tab tilt-b" style="left:612px;">Workshops</a>
        <a class="nav-tab tilt-a" style="left:753px;">Members<br>/Board</a>
        <a class="nav-tab tilt-b" style="left:894px;">Sponsors</a>
      </nav>
      <div class="hero-photo hands-feet" role="img" aria-label="Black and white photo of a mother's hands forming a heart around a baby's feet"></div>
      <h1 class="tagline">Help us help our sisters and daughters to take back control over how we bring the next generation to life.</h1>
      <div class="hero-photo expecting-mother" role="img" aria-label="Black and white photo of an expecting mother holding her belly"></div>
    </header>

    <main class="content">
      <div class="intro">
        <p>Lorem ipsum dolor sit amet, consetetur sadipscing elitr, sed diam nonumy eirmod<br>tempor invidunt ut labore et dolore magna aliquyam erat, sed diam voluptua. At vero<br>eos et accusam et justo duo dolores et ea rebum. Stet clita kasd gubergren, no sea<br>takimata sanctus est Lorem ipsum dolor sit amet. Lorem ipsum dolor sit amet, consetetur<br>sadipscing elitr, sed diam nonumy eirmod tempor invidunt ut labore et dolore magna<br>aliquyam erat, sed diam voluptua. At vero eos et accusam et justo duo dolores et ea rebum.<br>Stet clita kasd gubergren, no sea takimata sanctus est Lorem ipsum dolor sit amet. Lorem<br>ipsum dolor sit amet, consetetur sadipscing elitr, sed diam nonumy eirmod tempor invidunt<br>ut labore et dolore magna aliquyam erat, sed diam voluptua. At vero eos et accusam et justo<br>duo dolores et ea rebum. Stet clita kasd gubergren, no sea takimata sanctus est Lorem<br>ipsum dolor sit amet.</p>
        <p>Lorem ipsum dolor sit amet, consetetur sadipscing elitr, sed diam nonumy eirmod<br>tempor invidunt ut labore et dolore magna aliquyam erat, sed diam voluptua. At vero<br>eos et accusam et justo duo dolores et ea rebum. Stet clita kasd gubergren, no sea<br>takimata sanctus est Lorem ipsum dolor sit amet. Lorem ipsum dolor sit amet, consetetur<br>sadipscing elitr, sed diam nonumy eirmod tempor invidunt ut labore et dolore magna<br>aliquyam erat, sed diam voluptua. At vero eos et accusam et justo duo dolores et ea rebum.<br>Stet clita kasd gubergren, no sea takimata sanctus est Lorem ipsum dolor sit amet. Lorem<br>ipsum dolor sit amet, consetetur sadipscing elitr, sed diam nonumy eirmod tempor invidunt<br>ut labore et dolore magna aliquyam erat, sed diam voluptua. At vero eos et accusam et justo<br>duo dolores et ea rebum. Stet clita kasd gubergren, no sea takimata sanctus est Lorem<br>ipsum dolor sit amet.</p>
      </div>

      <aside class="feature-list">
        <div class="feature">
          <span class="feature-photo outreach" role="img" aria-label="Photo of hands holding a green glass globe"></span>
          <div class="feature-caption">International Outreach</div>
        </div>
        <div class="feature">
          <span class="feature-photo volunteers" role="img" aria-label="Photo of a newborn's hand held by an adult hand"></span>
          <div class="feature-caption">Volunteers</div>
        </div>
        <div class="feature">
          <span class="feature-photo news" role="img" aria-label="Photo of rolled newspapers"></span>
          <div class="feature-caption">News and Events</div>
        </div>
      </aside>
    </main>

    <footer class="site-footer">
      <p class="copyright">All Content Copyright © 2009 AMBER TIDE ALLIANCE. All Rights Reserved.</p>
    </footer>
  </div>
</body>
</html>
```